Packaging for Portable Bidet Product

Product:
Our product, Swishka, is a portable hand bidet. What is a portable hand bidet as some may ask? It is small water bottle with a nozzle head that is used to wash “bottoms” after going “poo-poo” (pardon our crudeness). Bidets are popular in European, Asian and African markets and are used alongside toilet paper to give a truly fresh and clean experience. Besides cleanliness, bidets are eco-friendly (they reduce toilet paper usage by x%) and are perfect for travel.
Current Competition + Role of Packaging:
We are launching our portable bidet product in the US market, primarily to be sold via Marketvale. There are currently some existing players in the market, but we’ve done our research and created a product that is superior in functionality and style. That being said, our competitors still have a first-mover advantage and have amassed a high volume of Marketvale ratings, hence we have a bit of a challenge which we feel that can be easily tackled with premium branding and marketing.
That being said, we are looking for a packaging design that:
i. Distinguishing our product on Marketvale (meaning, the packaging looks good in photos)
ii. Highlight that ours is a premium product
Our design values:
‘Hygiene meets modern design’. Some adjectives that describe our brand -
• Clean
• Fresh
• Simple
• Quirky
• Premium
• Discreet
• Subtle
Attachments:
• Our packaging dimensions (see attached)
• Our brand color (Pantone 331C)
• Our logo file (see attached file)
• Product photos (see attached file)
• Illustration of our product instructions (see attached file)
• Packaging designs that inspire us (see attached file)
• Packaging designs of our competition for reference (see attached file)
• Content/text for the packaging box (see below)
What should be on the box:
• Logo and Brand Name
• Product Photo (can be an outline/illustration as well)
• Product instructions illustration (see attached file)
• Text to be included in packaging
o Product description – “A Modern Portable Bidet”
o Bottle size – 400ml
o Key features
Anti-leak
Discreet design
Travel friendly size
Angled spray
Eco-friendly
Easy squeeze bottle
Includes travel bag
Target Market(s)
The product is aimed at both men and women (of all ages) in the US and Canada markets. In terms of audience targets, we will be appealing to outdoor enthusiasts, immigrants abroad, new parents (product to be used to clean their babies), patients (people with limited mobility) and eco-conscious consumers.
Industry/Entity Type
Health And Wellness

```html
<!DOCTYPE html>
<html lang="en">
<head>
<meta charset="utf-8">
<title>Swishka Portable Hand Bidet – Packaging</title>
<link rel="stylesheet" href="https://fonts.googleapis.com/css2?family=Russo+One&family=Pathway+Gothic+One&family=Baloo+2:wght@600&display=swap">
<style>
  :root {
    --bg: #efeeec;
    --panel: #b9d6d1;
    --panel-edge: #a9cbc5;
    --brand: #76bcb0;
    --brand-deep: #5fae9f;
    --ink: #111111;
    --white: #ffffff;
    --tab-shadow: rgba(40, 70, 65, 0.35);
  }
  * { box-sizing: border-box; margin: 0; padding: 0; }
  html, body { width: 1200px; height: 1200px; overflow: hidden; background: var(--bg); }
  .dieline {
    position: absolute; left: 200px; top: 60px;
    display: flex; height: 1080px;
  }
  .panel { position: relative; height: 100%; background: var(--panel); }
  .panel--side { width: 300px; border-right: 1px solid var(--panel-edge); }
  .panel--front { width: 500px; }

  .brand-name {
    font-family: "Russo One", sans-serif;
    font-size: 30px; letter-spacing: 0.5px;
    display: flex; flex-direction: column; align-items: center; gap: 12px;
  }
  .brand-name .dot { width: 56px; height: 56px; border-radius: 50%; border: 0; }
  .panel--side .brand-name { position: absolute; top: 150px; left: 0; right: 0; color: var(--white); }
  .panel--side .brand-name .dot { background: var(--white); }
  .panel--front .brand-name { position: absolute; top: 70px; left: 0; right: 0; color: var(--brand); }
  .panel--front .brand-name .dot { background: var(--brand); }

  .features { position: absolute; top: 340px; left: 18px; list-style: none; }
  .feature {
    width: 236px; height: 60px; margin-bottom: 18px;
    background: linear-gradient(90deg, #f4f4f4, #ffffff 60%, #e9e9e9);
    border-radius: 4px 30px 30px 4px;
    box-shadow: 4px 8px 10px var(--tab-shadow);
    font-family: "Pathway Gothic One", sans-serif;
    font-size: 27px; color: var(--ink);
    display: flex; align-items: center; padding-left: 16px;
  }

  .side-band {
    position: absolute; left: 0; right: 0; bottom: 0; height: 220px;
    background: var(--brand);
    color: var(--white);
    font-family: "Pathway Gothic One", sans-serif;
    padding: 40px 0 0 40px;
  }
  .side-band .line1 { font-size: 40px; line-height: 1; }
  .side-band .line2 { font-size: 56px; line-height: 1.1; }

  .title { position: absolute; top: 300px; left: 62px; font-family: "Russo One", sans-serif; color: var(--ink); }
  .title .line1 { font-size: 40px; line-height: 1; }
  .title .line2 { font-size: 58px; line-height: 1.15; }

  .product-visual {
    position: absolute; top: 420px; left: 50px; width: 400px; height: 500px;
    background: radial-gradient(ellipse at 50% 55%, #7fc6b6 0 18%, #cfe6e2 40%, rgba(185,214,209,0) 70%);
  }
  .audience {
    position: absolute; top: 950px; left: 0; right: 0; text-align: center;
    font-family: "Baloo 2", sans-serif; font-weight: 600;
    font-size: 24px; color: var(--brand-deep);
  }
  .volume {
    position: absolute; top: 1000px; right: 30px;
    font-family: "Baloo 2", sans-serif; font-weight: 600;
    font-size: 28px; color: var(--ink);
  }
</style>
</head>
<body>
  <main class="dieline">
    <section class="panel panel--side">
      <div class="brand-name"><span class="dot"></span>Swishka</div>
      <ul class="features">
        <li class="feature">Anti-leak</li>
        <li class="feature">Discreet design</li>
        <li class="feature">Travel friendly size</li>
        <li class="feature">Angled spray</li>
        <li class="feature">Eco-friendly</li>
        <li class="feature">Easy squeeze bottle</li>
        <li class="feature">Includes travel bag</li>
      </ul>
      <div class="side-band">
        <div class="line1">Portable</div>
        <div class="line2">Hand Bidet</div>
      </div>
    </section>

    <section class="panel panel--front">
      <div class="brand-name"><span class="dot"></span>Swishka</div>
      <h1 class="title">
        <div class="line1">Portable</div>
        <div class="line2">Hand Bidet</div>
      </h1>
      <div class="product-visual" role="img" aria-label="Teal squeeze bottle bidet with white telescopic nozzle surrounded by a clear water splash"></div>
      <p class="audience">For man and women</p>
      <p class="volume">400ml</p>
    </section>
  </main>
</body>
</html>
```